Creative Flyer Design Project

I want to create a flyer. I have attached wireframe (wireframe.png) of flyer which gives you much needed idea regarding flyer content. I have attached few images from our portfolio which can be used while designing a flyer.

I would like you to show me the extreme creativity and capability in delivering world class flyer design.

No heavy graphics needed. I want extremely clean and professional flyer using icons, colors and highlighted text/headings.

I will be requiring multiple formats of flyer such as .ai/.png/.psd/pdf.

Size of flyer: Standard A4 size OR Height is at discretion of designer. The width must be below 780 px.

Fonts to be used: Web 2.0 fonts needed. Must drive message clearly.

*** Long term association oppurtunity exists for the right creative designers for direct work

Target Market(s)

Business owners

Industry/Entity Type

Work

Requirements
Should not have
• Cartoonish or cheap graphics

```html
<!DOCTYPE html>
<html lang="en">
<head>
<meta charset="utf-8">
<title>BrightMark Design Services Flyer</title>
<link rel="stylesheet" href="https://fonts.googleapis.com/css2?family=Oswald:wght@500;700&family=Open+Sans:wght@400;600&family=Arimo:wght@400;700&display=swap">
<style>
:root{
  --ink:#1e1e1e;
  --white:#ffffff;
  --lime:#a7c332;
  --lime-dark:#7fa01e;
  --lime-light:#c6dc5a;
  --band:#9dbb2f;
  --red:#c8202f;
  --text-dark:#222222;
  --panel:#c9cbcc;
}
*{margin:0;padding:0;box-sizing:border-box}
html,body{width:764px;height:1200px;overflow:hidden;background:var(--ink)}
.flyer{position:relative;width:764px;height:1200px;background:var(--ink);font-family:"Arimo",Arial,sans-serif;color:var(--white)}
.abs{position:absolute}
.headline-top{top:12px;left:0;width:764px;text-align:center;font-family:"Oswald",sans-serif;font-weight:700;font-size:31px;letter-spacing:.5px}
.headline-main{top:46px;left:0;width:764px;text-align:center;font-family:"Oswald",sans-serif;font-weight:700;font-size:56px;line-height:1.1;color:var(--lime);letter-spacing:1px}
.subline{top:114px;left:0;width:764px;text-align:center;font-family:"Open Sans",sans-serif;font-size:25px}
.category .tab{position:absolute;top:0;left:0;height:35px;background:linear-gradient(var(--lime-light),var(--lime-dark));font-family:"Oswald",sans-serif;font-weight:500;font-size:17px;line-height:35px;padding-left:12px;clip-path:polygon(3% 0,100% 0,93% 100%,0 100%)}
.category .box{position:absolute;top:35px;left:0;right:0;height:174px;background:var(--white);border:2px solid #dadada;padding:10px 8px 0 8px;display:flex;gap:4px}
.category ul{list-style:none;flex:1}
.category li{font-size:10px;line-height:17.4px;color:var(--text-dark);white-space:nowrap}
.category li::before{content:"> ";color:#4a78a8}
.green-band{top:381px;left:0;width:764px;height:276px;background:linear-gradient(var(--band),#8fad25)}
.section-title{font-family:"Oswald",sans-serif;font-weight:700;font-size:21px;line-height:27px;text-transform:uppercase}
.benefits{top:392px;left:23px;width:330px}
.benefits ul{list-style:none;margin-top:14px}
.benefits li{font-size:11.5px;font-weight:700;line-height:15px;margin-bottom:5px;padding-left:15px;position:relative}
.benefits li::before{content:"";position:absolute;left:3px;top:3px;width:5px;height:8px;border-radius:2px;background:#d9ebf7}
.process{top:392px;left:371px;width:380px}
.process ol{list-style:none;margin-top:10px}
.process li{font-size:11.5px;font-weight:700;line-height:14px;position:relative;margin-bottom:12px;padding-left:2px}
.process li:not(:last-child)::after{content:"";position:absolute;left:122px;bottom:-9px;border-left:6px solid transparent;border-right:6px solid transparent;border-top:5px solid var(--white);opacity:.9}
.formats{top:609px;left:375px;display:flex;gap:20px}
.format{width:32px;height:39px;background:var(--white);border-radius:3px;position:relative;box-shadow:0 1px 2px rgba(0,0,0,.3)}
.format span{position:absolute;bottom:3px;left:2px;right:2px;height:12px;font-size:9px;line-height:12px;text-align:center;color:var(--white);font-weight:700}
.portfolio-tab{top:635px;left:58px;width:236px;height:33px;background:var(--ink);font-family:"Oswald",sans-serif;font-weight:700;font-size:25px;line-height:33px;color:var(--lime);padding-left:10px;clip-path:polygon(0 0,100% 0,100% 100%,0 100%)}
.portfolio-frame{top:668px;left:60px;width:642px;height:258px;border-radius:14px;background:linear-gradient(var(--lime),#2aa1b3);padding:4px}
.portfolio-art{width:100%;height:100%;border-radius:11px;background:linear-gradient(135deg,#d4d6d7,var(--panel) 50%,#b6b8b9)}
.partner-banner{top:942px;left:55px;width:643px;height:40px;background:linear-gradient(#d42a37,#a81624);clip-path:polygon(2% 0,100% 0,98% 100%,0 100%);font-family:"Oswald",sans-serif;font-weight:700;font-size:23px;line-height:40px;text-align:center}
.badge{top:989px;left:63px}
.call{top:987px;left:0;width:764px;text-align:center;font-size:15px;padding-left:10px}
.contact{font-size:15px;display:flex;align-items:center;gap:8px}
.contact .service{font-weight:700;font-size:12px;color:var(--lime)}
.discount-bar{top:1105px;left:34px;width:686px;height:37px;background:var(--lime);font-family:"Oswald",sans-serif;font-weight:700;font-size:21px;line-height:37px;padding-left:26px;display:flex;gap:24px}
.site-logo{top:1150px;left:64px;font-family:"Open Sans",sans-serif;font-size:24px}
.visit{top:1157px;left:322px;font-size:15px}
</style>
</head>
<body>
<div class="flyer">
  <h1 class="abs headline-top">100% CUSTOM GRAPHIC DESIGNS AT THE</h1>
  <h2 class="abs headline-main">MOST AFFORDABLE PRICES</h2>
  <p class="abs subline">Our services are available in 36 design categories</p>

  <section class="abs category" style="top:158px;left:10px;width:188px;">
    <div class="tab" style="width:178px">CORPORATE IDENTITY</div>
    <div class="box" style="left:6px">
      <ul>
        <li>Logo design</li><li>Stationery design</li><li>Business card design</li><li>Envelope design</li><li>Letterhead design</li><li>Presentation folder design</li><li>Power point template design</li>
      </ul>
    </div>
  </section>

  <section class="abs category" style="top:158px;left:212px;width:258px;">
    <div class="tab" style="width:214px">GRAPHICS / PRINT DESIGN</div>
    <div class="box" style="left:10px">
      <ul>
        <li>T-shirt design</li><li>Brochure design</li><li>Poster design</li><li>Postcard design</li><li>Flyer design</li><li>Book cover design</li><li>Label / Sticker design</li><li>CD cover design</li><li>Trade show display</li>
      </ul>
      <ul>
        <li>Signage design</li><li>Newspaper ad design</li><li>Greeting card /</li><li>Invitation design</li><li>Packaging design</li><li>Vehicle wrap design</li><li>Shopping bag design</li><li>Door hanger design</li><li>Certificate design</li>
      </ul>
    </div>
  </section>

  <section class="abs category" style="top:158px;left:482px;width:264px;">
    <div class="tab" style="width:272px">WEB DESIGN &amp; DEVELOPMENT</div>
    <div class="box" style="left:10px">
      <ul>
        <li>Landing page design</li><li>Web page design</li><li>Ecommerce web design</li><li>Blog design</li><li>CMS website design</li><li>Newsletter design</li>
      </ul>
      <ul>
        <li>Banner ad design</li><li>Social page design</li><li>Microblog page design</li><li>Video channel page</li><li>Community page design</li>
      </ul>
    </div>
  </section>

  <div class="abs green-band"></div>

  <section class="abs benefits">
    <h3 class="section-title">Benefits you get by dealing with<br>BRIGHTMARK.COM</h3>
    <ul>
      <li>Creatively crafted functional designs</li>
      <li>Highly affordable pricing</li>
      <li>Multiple variations of designs submitted</li>
      <li>Variations open to revisions</li>
      <li>Guaranteed 48 hours delivery</li>
      <li>30000+ ready designs also available, all open for 100% customization at no extra cost</li>
    </ul>
  </section>

  <section class="abs process">
    <h3 class="section-title">Our design process</h3>
    <ol>
      <li>Careful analysis of your individual &amp; business needs</li>
      <li>Creation of rough hand drawn sketches</li>
      <li>Analyzing sketches &amp; shortlisting them</li>
      <li>Conversion of shortlisted hand drawn sketches to digital formats</li>
      <li>Submission of multiple variations of designs to choose from</li>
      <li>Feedback/suggestions rounds to give final shape to your design</li>
      <li>Delivery of design in multiple digital formats</li>
    </ol>
  </section>

  <div class="abs formats">
    <div class="format"><span style="background:#2f6db3">PSD</span></div>
    <div class="format"><span style="background:#e58a1f">PNG</span></div>
    <div class="format"><span style="background:#3f86c6">JPG</span></div>
    <div class="format"><span style="background:#e07a1a">EPS</span></div>
    <div class="format"><span style="background:#5a9b2e">CDR</span></div>
    <div class="format"><span style="background:#d3262c">PDF</span></div>
    <div class="format"><span style="background:#ef7f1a">AI</span></div>
  </div>

  <div class="abs portfolio-tab">OUR WORK PORTFOLIO</div>
  <div class="abs portfolio-frame">
    <div class="portfolio-art" role="img" aria-label="Collage of portfolio pieces: letterhead, business cards, software box, book cover, CD, websites, shopping cart and social page designs"></div>
  </div>

  <div class="abs partner-banner">PREFERRED PARTNER FOR 5000+ INDIVIDUALS &amp; BUSINESSES</div>

  <svg class="abs badge" width="100" height="100" viewBox="0 0 100 100" aria-label="100% satisfaction guaranteed">
    <circle cx="50" cy="48" r="46" fill="#c8202f"/>
    <circle cx="50" cy="48" r="40" fill="#ffffff"/>
    <path d="M2 62 L98 62 L92 72 L98 82 L2 82 L8 72 Z" fill="#b01a27"/>
    <text x="50" y="45" text-anchor="middle" font-family="Oswald,sans-serif" font-weight="700" font-size="30" fill="#c8202f">100<tspan font-size="12">%</tspan></text>
    <text x="50" y="58" text-anchor="middle" font-family="Arimo,sans-serif" font-weight="700" font-size="9" fill="#c8202f">SATISFACTION</text>
    <text x="50" y="76" text-anchor="middle" font-family="Arimo,sans-serif" font-weight="700" font-size="7" fill="#ffffff">GUARANTEED</text>
  </svg>

  <p class="abs call">Call us now: +11 55501 24680</p>
  <div class="abs contact" style="top:1026px;left:222px"><span class="service">TalkLine</span>xxxxxxxxxxxxxxxxx</div>
  <div class="abs contact" style="top:1026px;left:439px"><span class="service">CallWave</span>yyyyyyyyyyy</div>
  <div class="abs contact" style="top:1061px;left:205px"><span class="service">MsgNet</span>info@brightmark.com</div>
  <div class="abs contact" style="top:1061px;left:441px"><span class="service">YoMail</span>zzzzzzzzzzz</div>

  <div class="abs discount-bar"><span>21% SPECIAL DISCOUNT FOR OUR ABCDEFG MEMBERS</span><span>Use » zzzzzzz2013</span></div>

  <div class="abs site-logo">Site logo</div>
  <p class="abs visit">Visit www.brightmark.com today!</p>
</div>
</body>
</html>
```